Education business partners flyer

Our service is New Zealand education and migration. We are trying to recruit business partners from around the world who can refer clients to us. We need a 2-3 page PDF flyer that we want to share with our prospective partners. Our content is ready (file attached). It needs to be designed well with relevant NZ images, international students/migrants and our logo of course.

Target Market(s)

All around the world

Industry/Entity Type

Education

Font styles to use
Sans Serif

Colors

Designer to choose colors to be used in the design.

Requirements
Must have
• It needs to be designed well with relevant NZ images, international students/migrants and our logo of course.
Nice to have
• Copyright free images.
Should not have
• Images with any copyright issues.

```html
<!DOCTYPE html>
<html lang="en">
<head>
<meta charset="utf-8">
<title>Moriva Partnership Proposal</title>
<link rel="stylesheet" href="https://fonts.googleapis.com/css2?family=Open+Sans:ital,wght@0,400;0,600;0,700;0,800;1,700;1,800&display=swap">
<style>
  :root {
    --purple: #7a1a86;
    --purple-soft: rgba(153, 51, 168, 0.85);
    --ink: #1d1d1d;
    --body: #3a3a3a;
    --page: #ffffff;
    --backdrop: #cfcfcf;
    --muted: #ececec;
  }
  * { box-sizing: border-box; margin: 0; padding: 0; }
  html, body { width: 1200px; height: 800px; overflow: hidden; }
  body {
    background: var(--backdrop);
    font-family: "Open Sans", Arial, sans-serif;
    color: var(--body);
  }
  .spread {
    position: relative;
    width: 1200px; height: 800px;
    display: flex; gap: 22px;
    justify-content: center; align-items: center;
  }
  .page {
    position: relative;
    width: 372px; height: 526px;
    background: var(--page);
    overflow: hidden;
  }

  /* Cover */
  .cover-photo {
    position: absolute; left: 0; top: 0; width: 100%; height: 380px;
    background: linear-gradient(180deg, #c4c4c4 0%, #e6e6e6 35%, #9e9e9e 55%, #d4d4d4 100%);
  }
  .brand {
    position: absolute; left: 24px; top: 26px;
    display: flex; align-items: center; gap: 7px;
    font-weight: 800; font-size: 22px; color: var(--ink);
  }
  .brand-dot { width: 14px; height: 14px; border-radius: 50%; background: var(--ink); }
  .intro-box {
    position: absolute; left: 196px; top: 136px; width: 176px; height: 196px;
    background: var(--purple-soft);
    padding: 14px 14px;
    color: #fff; font-size: 7.6px; line-height: 1.45; text-align: justify;
  }
  .intro-box p + p { margin-top: 7px; }
  .cover-title {
    position: absolute; left: 18px; top: 398px;
    font-style: italic; font-weight: 800; font-size: 44px; line-height: 0.82;
    letter-spacing: -0.5px;
  }
  .cover-title .accent { color: var(--purple); display: block; }
  .cover-title .dark { color: var(--ink); display: block; }

  /* Opportunity page */
  .section-heading {
    position: absolute; left: 0; right: 0; top: 20px;
    text-align: center; font-weight: 800; font-size: 15px; color: var(--ink);
    letter-spacing: 0.3px;
  }
  .qa-row {
    position: absolute; left: 18px; right: 18px;
    display: flex; gap: 12px; align-items: flex-start;
  }
  .qa-label {
    flex: 0 0 96px; text-align: right;
    font-style: italic; font-weight: 800; font-size: 13px; line-height: 1.1;
    color: var(--purple);
  }
  .qa-text { font-size: 7.2px; line-height: 1.45; color: var(--body); }
  .qa-why { top: 50px; }
  .group-photo {
    position: absolute; left: 0; top: 140px; width: 100%; height: 194px;
    background: linear-gradient(90deg, #8a8f9a 0%, #5d6470 40%, #b9b3a8 70%, #d8cf8f 100%);
  }
  .photo-notch { position: absolute; left: 170px; top: 333px; }
  .lower-band {
    position: absolute; left: 0; top: 342px; width: 100%; height: 184px;
    background: linear-gradient(180deg, #f4f4f4, var(--muted));
  }
  .qa-framework { top: 382px; }

  /* Strengths page */
  .strengths-wash {
    position: absolute; left: 0; top: 0; width: 100%; height: 230px;
    background: linear-gradient(180deg, #dcdcdc 0%, #f3f3f3 70%, #ffffff 100%);
  }
  .edge-bar {
    position: absolute; left: 0; top: 176px; width: 6px; bottom: 0;
    background: var(--purple);
  }
  .strengths-title {
    position: absolute; left: 30px; top: 86px;
    font-style: italic; font-weight: 800; font-size: 23px; line-height: 1.05;
  }
  .strengths-title .accent { color: var(--purple); display: block; }
  .strengths-title .dark { color: var(--ink); display: block; }
  .strengths-grid {
    position: absolute; left: 30px; right: 18px; top: 176px;
    display: grid; grid-template-columns: 1fr 1fr; column-gap: 22px; row-gap: 18px;
  }
  .strength h3 {
    font-size: 7.4px; font-weight: 700; line-height: 1.2;
    color: var(--purple); text-transform: uppercase; margin-bottom: 4px;
  }
  .strength p { font-size: 6.8px; line-height: 1.45; color: var(--body); }
</style>
</head>
<body>
<main class="spread">

  <section class="page cover">
    <div class="cover-photo" role="img" aria-label="Black and white New Zealand mountain valley with an open road"></div>
    <div class="brand"><span class="brand-dot"></span>Moriva</div>
    <div class="intro-box">
      <p>New Zealand is booming as an education &amp; migration destination. In a world that is spiralling out of control; the serenity, safety and opportunities of New Zealand are attracting people from everywhere like a magnet. Numbers have been growing dramatically year on year.</p>
      <p>We are a deeply committed New Zealand education &amp; migration company, seeking to attract the best talent from around the world to make New Zealand their new home.</p>
    </div>
    <h1 class="cover-title"><span class="accent">PARTNERSHIP</span><span class="dark">PROPOSAL</span></h1>
  </section>

  <section class="page opportunity">
    <h2 class="section-heading">BUSINESS OPPORTUNITY</h2>
    <div class="qa-row qa-why">
      <h3 class="qa-label">Why collaborate with Moriva?</h3>
      <p class="qa-text">Collaborations can accelerate mutual growth in a globalised world. Our rationale in this proposal is that we do not have the reach in your market and vice versa you do not have a presence or team in New Zealand to continue to service your students or clients once they arrive here. By coming together we can achieve both these mutual objectives and create a viable and mutual business opportunity.</p>
    </div>
    <div class="group-photo" role="img" aria-label="Group of international students standing together in casual clothes"></div>
    <svg class="photo-notch" width="32" height="12" viewBox="0 0 32 12" aria-hidden="true"><polygon points="0,0 32,0 16,12" fill="#6f7480"/></svg>
    <div class="lower-band"></div>
    <div class="qa-row qa-framework">
      <h3 class="qa-label">What is the Moriva partnership framework?</h3>
      <p class="qa-text">We propose to work with you as our Referral Partner. A partnership that can be mutually beneficial and enhance the value of international education &amp; migration to deserving students and clients from everywhere. Our levels of association can vary depending on your current focus and how you can utilise our position especially in the areas of services that can only be rendered by a Licensed Immigration Adviser.</p>
    </div>
  </section>

  <section class="page strengths">
    <div class="strengths-wash" role="img" aria-label="Faint photo of a student jumping outdoors"></div>
    <div class="edge-bar"></div>
    <h2 class="strengths-title"><span class="accent">WHAT ARE THE</span><span class="dark">STRENGTHS OF MORIVA?</span></h2>
    <div class="strengths-grid">
      <article class="strength">
        <h3>We are New Zealand owned and based:</h3>
        <p>Hence we are able to provide services to clients in an end-to-end fashion from suggesting the right courses at the very beginning of their journey to hand-holding them all the way to employment and eventual residency in New Zealand. By working with us you not only create a viable business opportunity but can also be assured that your students/clients are in safe hands after they reach New Zealand. This is where the real challenges start for these young people as they need a huge amount of onshore support and guidance which we can provide.</p>
      </article>
      <article class="strength">
        <h3>We have the full range of institutions:</h3>
        <p>We represent the entire gamut of quality New Zealand institutions and in the event your student needs/deserves the appropriate institution to fulfill their future aspirations, we can provide this opportunity for them together. We believe each student deserves to be in the institution that best serves their future interests and we can provide this opportunity for them.</p>
      </article>
      <article class="strength">
        <h3>We have an experienced team and great software:</h3>
        <p>Our competent counseling team backed by a visa team (including ex New Zealand immigration staff) uses modern case software, so every file is tracked clearly and partners always know where their clients stand.</p>
      </article>
      <article class="strength">
        <h3>We have a very high visa success rate:</h3>
        <p>Our current visa success rate for the first quarter of 2018 sits well above 90% and we are proud that it has been improving on it steadily every year.</p>
      </article>
    </div>
  </section>

</main>
</body>
</html>
```